Two Web Banners Needed for children product website! Fun and colorful!

My website is www.brightpebbletrinkets.com.au

I want 2 banners for the home page.

Size: 1920x1080px

Colors I like:
#BBA5D0
#FBF5BC
#F2BBAD

Text:
1) We create unique and meaningful gifts
2) We help you create happy memories

Fonts: provided in link

Brief:
1) I need two banners that showcase my two products on my website. I have images and fonts are included you can use in the files.
2) I want to capture child nature, friendliness and happiness.
3) I have also included samples of what I like
4) It's important to use some of the customer photographs too

Link to files:
https://filedrop-example.net/downloads/a1b2c3d4e5f60718293a4b5c6d7e8f9020220101000000/0f1e2d3c4b5a69788796a5b4c3d2e1f020220101000001/9z8y7x

If link does not work please PM me

Target Market(s)

Parents of children

Industry/Entity Type

Children ecommerce

Font styles to use
Other font styles liked:
• in file

Requirements
Must have
• Clean modern look

```html
<!DOCTYPE html>
<html lang="en">
<head>
<meta charset="utf-8">
<title>Bright Pebble Trinkets – Unique &amp; Meaningful Gifts</title>
<link rel="stylesheet" href="https://fonts.googleapis.com/css2?family=Great+Vibes&family=Righteous&family=Stint+Ultra+Condensed&display=swap">
<style>
  :root {
    --cream: #faf4b9;
    --cream-deep: #f3eca9;
    --ink: #0b0b0b;
    --sage: #bab795;
    --plum: #521a40;
    --berry: #8e1632;
    --lilac: #bba5d0;
    --blush: #f2bbad;
    --cloud: #ffffff;
  }
  html, body {
    margin: 0;
    padding: 0;
    width: 1200px;
    height: 675px;
    overflow: hidden;
    background: var(--cream);
  }
  .banner {
    display: block;
    width: 1200px;
    height: 675px;
  }
  .headline-small { font-family: "Stint Ultra Condensed", serif; fill: var(--ink); }
  .headline-big { font-family: "Righteous", sans-serif; fill: var(--ink); }
  .headline-amp { font-family: "Great Vibes", cursive; fill: var(--ink); }
</style>
</head>
<body>
<svg class="banner" viewBox="0 0 1920 1080" xmlns="http://www.w3.org/2000/svg">
  <defs>
    <linearGradient id="sage-chair" x1="0" y1="0" x2="0" y2="1">
      <stop offset="0" stop-color="#d8d6a6"/><stop offset="1" stop-color="#c9c591"/>
    </linearGradient>
    <linearGradient id="lilac-chair" x1="0" y1="0" x2="0" y2="1">
      <stop offset="0" stop-color="#c7a6d6"/><stop offset="1" stop-color="#b894c6"/>
    </linearGradient>
    <linearGradient id="plum-chair" x1="0" y1="0" x2="0" y2="1">
      <stop offset="0" stop-color="#7d3166"/><stop offset="1" stop-color="#5e1d4c"/>
    </linearGradient>
    <linearGradient id="berry-chair" x1="0" y1="0" x2="0" y2="1">
      <stop offset="0" stop-color="#b51f3a"/><stop offset="1" stop-color="#9c1830"/>
    </linearGradient>
    <linearGradient id="child-yellow" x1="0" y1="0" x2="0" y2="1">
      <stop offset="0" stop-color="#f2bbad"/><stop offset="1" stop-color="#e4cf7a"/>
    </linearGradient>
    <linearGradient id="child-pink" x1="0" y1="0" x2="0" y2="1">
      <stop offset="0" stop-color="#bba5d0"/><stop offset="1" stop-color="#ee9fc0"/>
    </linearGradient>
  </defs>

  <rect class="backdrop" width="1920" height="1080" fill="var(--cream)"/>

  <!-- clouds -->
  <g class="cloud" fill="var(--cloud)">
    <circle cx="100" cy="115" r="36"/><circle cx="148" cy="105" r="38"/><circle cx="192" cy="118" r="24"/>
    <rect x="100" y="110" width="100" height="42" rx="21"/>
  </g>
  <g class="cloud" fill="var(--cloud)">
    <circle cx="876" cy="128" r="18"/><circle cx="900" cy="120" r="18"/><circle cx="920" cy="130" r="12"/>
    <rect x="862" y="126" width="68" height="20" rx="10"/>
  </g>

  <!-- stage on the right -->
  <ellipse class="stage" cx="1440" cy="900" rx="420" ry="62" fill="var(--cream-deep)"/>

  <!-- colour stripes -->
  <rect class="stripe stripe-sage" x="1188" y="0" width="124" height="600" fill="var(--sage)"/>
  <rect class="stripe stripe-plum" x="1373" y="0" width="124" height="600" fill="var(--plum)"/>
  <rect class="stripe stripe-berry" x="1559" y="0" width="124" height="600" fill="var(--berry)"/>

  <!-- headline -->
  <text class="headline-small" x="160" y="183" font-size="84" textLength="272" lengthAdjust="spacingAndGlyphs">we create</text>
  <text class="headline-big" x="160" y="365" font-size="225" textLength="622" lengthAdjust="spacingAndGlyphs">UNIQUE</text>
  <text class="headline-amp" x="796" y="368" font-size="120">&amp;</text>
  <text class="headline-small" x="160" y="505" font-size="160" textLength="697" lengthAdjust="spacingAndGlyphs">meaningful gifts</text>

  <!-- decorative dots and rings -->
  <circle cx="1023" cy="308" r="65" fill="none" stroke="var(--sage)" stroke-width="8"/>
  <circle cx="972" cy="556" r="43" fill="var(--berry)"/>
  <circle cx="159" cy="585" r="28" fill="var(--plum)"/>
  <circle cx="649" cy="571" r="12" fill="none" stroke="var(--berry)" stroke-width="2.5"/>
  <circle cx="291" cy="619" r="12" fill="none" stroke="var(--plum)" stroke-width="2.5"/>
  <circle cx="768" cy="651" r="12" fill="var(--plum)"/>
  <polygon class="star" fill="var(--ink)" points="458,558 465,576 484,577 469,589 474,607 458,597 442,607 447,589 432,577 451,576"/>

  <!-- photo areas, left group -->
  <g role="img" aria-label="Smiling toddler in a yellow dress sitting in front of a pink flower shape">
    <rect x="112" y="650" width="218" height="338" rx="40" fill="url(#child-yellow)"/>
  </g>
  <g role="img" aria-label="Sage linen children's chair embroidered with a name">
    <rect x="300" y="635" width="215" height="350" rx="14" fill="url(#sage-chair)"/>
  </g>
  <g role="img" aria-label="Lilac children's chair embroidered with a name">
    <rect x="545" y="635" width="207" height="350" rx="14" fill="url(#lilac-chair)"/>
  </g>
  <g role="img" aria-label="Baby in a pink bodysuit sitting in front of a lilac star shape">
    <rect x="705" y="685" width="248" height="335" rx="40" fill="url(#child-pink)"/>
  </g>

  <!-- photo areas, right group -->
  <g role="img" aria-label="Sage linen children's chair embroidered with a name">
    <rect x="1052" y="570" width="278" height="375" rx="16" fill="url(#sage-chair)"/>
  </g>
  <g role="img" aria-label="Plum children's chair embroidered with a name">
    <rect x="1318" y="570" width="237" height="372" rx="16" fill="url(#plum-chair)"/>
  </g>
  <g role="img" aria-label="Red children's chair embroidered with a name">
    <rect x="1550" y="570" width="275" height="375" rx="16" fill="url(#berry-chair)"/>
  </g>
</svg>
</body>
</html>
```